Company identity deisgn should support 2 languages

I would like to get our company identity design
This includes the following only
Business Cards 2 languages Arabic and English
Email signature
Letterhead
LinkUp profile images
Attached is the logo in Ai format

Requirements
Must have
• For business card
Must have
Name and Adrees in arabic
Name and Address in english
You might use both side of the card
Should not have
• Any pictures other than the logo

```html
<!DOCTYPE html>
<html lang="en">
<head>
<meta charset="utf-8">
<title>Nexora Cognitive Systems — Identity Set</title>
<link href="https://fonts.googleapis.com/css2?family=Roboto:wght@400;500;700&family=Tajawal:wght@400;500;700&display=swap" rel="stylesheet">
<style>
:root{
  --board:#737373;
  --blue:#1275bd;
  --blue-dark:#0c5c9c;
  --grey-bar:#6d6e71;
  --ink:#3d3d3d;
  --muted:#9a9a9a;
  --paper:#ffffff;
  --label:#ffffff;
}
*{box-sizing:border-box;margin:0;padding:0}
html,body{width:1200px;height:1200px;overflow:hidden}
body{background:var(--board);font-family:"Roboto",Arial,sans-serif;color:var(--ink);position:relative}
.piece{position:absolute;background:var(--paper);overflow:hidden;box-shadow:0 2px 6px rgba(0,0,0,.25)}
.label{position:absolute;color:var(--label);font-weight:700;font-size:13px;letter-spacing:.2px;transform:translateX(-50%);white-space:nowrap}
.ar{font-family:"Tajawal",Arial,sans-serif;direction:rtl}

/* logo lockup */
.logo{position:absolute;display:flex;align-items:center;gap:6px;color:var(--blue);font-weight:500;white-space:nowrap}
.logo .dot{border-radius:50%;background:var(--blue);flex:none}

/* footer band */
.band{position:absolute;left:0;right:0;display:flex}
.band .web{background:var(--blue);color:#fff;font-size:7px;letter-spacing:2px;display:flex;align-items:center;padding-left:37px;flex:0 0 78%;clip-path:polygon(0 0,100% 0,97% 100%,0 100%)}
.band .tail{background:var(--grey-bar);flex:1;margin-left:-8px}

/* contact list */
.contacts{position:absolute;font-size:7px;line-height:9.4px;color:var(--ink)}
.contacts li{list-style:none;display:flex;align-items:center;gap:4px}
.contacts svg{width:6px;height:6px;fill:var(--blue);flex:none}
.contacts.rtl li{flex-direction:row-reverse;justify-content:flex-start}
.addr{position:absolute;font-size:7px;line-height:9.4px}
.divider{position:absolute;width:1px;background:#d5d5d5}
.person .name{color:var(--blue);font-weight:700;font-size:10.5px;letter-spacing:.2px}
.person .role{color:var(--muted);font-size:7px}
.person .name-ar{color:var(--blue);font-family:"Tajawal",Arial,sans-serif;font-weight:700;font-size:11px}
.person .role-ar{color:var(--muted);font-family:"Tajawal",Arial,sans-serif;font-size:7.5px}
.row-contacts{position:absolute;left:16px;right:16px;display:flex;gap:4px;font-size:7px;color:var(--ink);align-items:center}
.row-contacts span{display:flex;align-items:center;gap:2px}
.row-contacts svg{width:6px;height:6px;fill:var(--blue)}

/* cards */
.card{border-radius:0 0 10px 10px}

/* social covers */
.cover{background:var(--blue);color:#fff}
.cover .tab{position:absolute;left:17px;top:0;width:177px;height:57px;background:#fff;border-radius:0 0 6px 6px}
.cover h2{position:absolute;left:18px;top:68px;font-size:22px;line-height:24px;font-weight:700}
.cover p{position:absolute;left:18px;top:124px;font-size:9.3px;line-height:11.8px;width:170px}
.art{position:absolute}

/* network profile */
.profile .banner{position:absolute;left:0;top:0;width:100%;height:132px;background:var(--blue)}
.profile h2{position:absolute;left:496px;top:34px;transform:translateX(-50%);color:#fff;font-size:32px;font-weight:700;white-space:nowrap}
.profile .sub{position:absolute;left:496px;top:72px;transform:translateX(-50%);color:#fff;font-size:13.5px;line-height:17px;text-align:center;white-space:nowrap}
.profile .avatar{position:absolute;left:17px;top:96px;width:78px;height:78px;background:linear-gradient(135deg,#fff,#c9c9c9);border:3px solid #fff;box-shadow:0 1px 3px rgba(0,0,0,.2);display:flex;align-items:center;justify-content:center}
.btn{position:absolute;top:186px;height:21px;font-size:11px;font-weight:700;display:flex;align-items:center;justify-content:center}
.btn.follow{left:17px;width:93px;background:var(--blue);color:#fff}
.btn.visit{left:119px;width:100px;border:1px solid var(--blue);color:var(--blue)}
.see-all{position:absolute;right:14px;top:193px;font-size:11px;font-weight:700;color:var(--blue)}
</style>
</head>
<body>

<svg width="0" height="0" style="position:absolute">
  <defs>
    <symbol id="i-phone" viewBox="0 0 10 10"><path d="M2 0.5l2 2-1 1.3c.6 1.3 1.6 2.3 2.9 2.9l1.3-1 2 2-1.3 1.8C4.5 9.2.8 5.5.3 1.8z"/></symbol>
    <symbol id="i-mobile" viewBox="0 0 10 10"><path d="M2.5 0h5v10h-5zM3.5 1v7h3V1z"/></symbol>
    <symbol id="i-fax" viewBox="0 0 10 10"><path d="M2.5 0h5v3h-5zM0 3.5h10V8H8v2H2V8H0zM3 6.5v2.5h4V6.5z"/></symbol>
    <symbol id="i-mail" viewBox="0 0 10 10"><path d="M0 2h10v6H0zM1 3v.3l4 2.5 4-2.5V3z"/></symbol>
  </defs>
</svg>

<!-- LETTERHEAD -->
<section class="piece letter" style="left:314px;top:55px;width:426px;height:596px;">
  <div class="logo" style="left:29px;top:42px;font-size:9px;"><span class="dot" style="width:16px;height:16px"></span>Nexora Cognitive Systems</div>
  <div class="addr" style="right:147px;top:31px;text-align:right;">
    <div class="ar">412 شارع الأرز</div>
    <div class="ar">بروكفيلد 52810</div>
    <div>412 Cedar Row</div>
    <div>Brookfield, Ontario 52810</div>
  </div>
  <div class="divider" style="left:288px;top:33px;height:38px"></div>
  <ul class="contacts" style="left:296px;top:35px;">
    <li><svg><use href="#i-phone"/></svg>555-014-2671</li>
    <li><svg><use href="#i-mobile"/></svg>555-018-3392</li>
    <li><svg><use href="#i-fax"/></svg>555-016-4470</li>
    <li><svg><use href="#i-mail"/></svg>hello@nexoracognitive.com</li>
  </ul>
  <div class="band" style="top:568px;height:14px;"><div class="web" style="padding-left:92px">WWW.NEXORACOGNITIVE.COM</div><div class="tail"></div></div>
</section>
<div class="label" style="left:527px;top:662px;">LETTER</div>

<!-- CARD FRONT -->
<section class="piece card" style="left:89px;top:161px;width:327px;height:186px;">
  <div class="logo" style="left:58px;top:29px;font-size:12px;"><span class="dot" style="width:24px;height:24px"></span>Nexora Cognitive Systems</div>
  <div class="person" style="position:absolute;right:189px;top:97px;text-align:right;">
    <div class="name">SAMER HADDAD</div>
    <div class="role">President</div>
  </div>
  <div class="divider" style="left:152px;top:77px;height:66px"></div>
  <div class="addr" style="left:166px;top:80px;"><div>412 Cedar Row</div><div>Brookfield, Ontario 52810</div></div>
  <ul class="contacts" style="left:166px;top:106px;">
    <li><svg><use href="#i-phone"/></svg>555-014-2671</li>
    <li><svg><use href="#i-mobile"/></svg>555-018-3392</li>
    <li><svg><use href="#i-fax"/></svg>555-016-4470</li>
    <li><svg><use href="#i-mail"/></svg>hello@nexoracognitive.com</li>
  </ul>
  <div class="band" style="top:158px;height:14px;"><div class="web">WWW.NEXORACOGNITIVE.COM</div><div class="tail"></div></div>
</section>
<div class="label" style="left:202px;top:362px;">FRONT</div>

<!-- CARD BACK -->
<section class="piece card" style="left:89px;top:388px;width:327px;height:186px;">
  <div class="logo" style="left:58px;top:29px;font-size:12px;"><span class="dot" style="width:24px;height:24px"></span>Nexora Cognitive Systems</div>
  <div class="addr ar" style="right:149px;top:77px;text-align:right;"><div>412 شارع الأرز</div><div>بروكفيلد 52810</div></div>
  <ul class="contacts rtl" style="right:149px;top:104px;">
    <li><svg><use href="#i-phone"/></svg>555-014-2671</li>
    <li><svg><use href="#i-mobile"/></svg>555-018-3392</li>
    <li><svg><use href="#i-fax"/></svg>555-016-4470</li>
    <li><svg><use href="#i-mail"/></svg>hello@nexoracognitive.com</li>
  </ul>
  <div class="divider" style="left:192px;top:74px;height:66px"></div>
  <div class="person" style="position:absolute;left:206px;top:96px;text-align:right;">
    <div class="name-ar">سامر حداد</div>
    <div class="role-ar">رئيس</div>
  </div>
  <div class="band" style="top:158px;height:14px;"><div class="web">WWW.NEXORACOGNITIVE.COM</div><div class="tail"></div></div>
</section>
<div class="label" style="left:199px;top:596px;">BACK</div>

<!-- EMAIL SIGNATURE 1 -->
<section class="piece sig" style="left:764px;top:298px;width:325px;height:157px;">
  <div class="person" style="position:absolute;left:20px;top:14px;">
    <div class="name">SAMER HADDAD</div>
    <div class="role">President</div>
    <div class="name-ar">سامر حداد</div>
    <div class="role-ar">رئيس</div>
  </div>
  <div class="addr" style="right:17px;top:13px;text-align:right;">
    <div class="ar">412 شارع الأرز</div><div class="ar">بروكفيلد 52810</div>
    <div style="margin-top:3px">412 Cedar Row</div><div>Brookfield, Ontario 52810</div>
  </div>
  <div class="logo" style="left:52px;top:70px;font-size:11px;"><span class="dot" style="width:22px;height:22px"></span>Nexora Cognitive Systems</div>
  <div class="row-contacts" style="top:117px;">
    <span><svg><use href="#i-phone"/></svg>555-014-2671</span>
    <span><svg><use href="#i-mobile"/></svg>555-018-3392</span>
    <span><svg><use href="#i-fax"/></svg>555-016-4470</span>
    <span><svg><use href="#i-mail"/></svg>hello@nexoracognitive.com</span>
  </div>
  <div class="band" style="top:137px;height:12px;"><div class="web" style="padding-left:64px">WWW.NEXORACOGNITIVE.COM</div><div class="tail"></div></div>
</section>
<div class="label" style="left:932px;top:469px;">EMAIL SIGNATURE 1</div>

<!-- EMAIL SIGNATURE 2 -->
<section class="piece sig" style="left:764px;top:495px;width:325px;height:156px;">
  <div class="logo" style="left:68px;top:17px;font-size:11px;"><span class="dot" style="width:22px;height:22px"></span>Nexora Cognitive Systems</div>
  <div class="addr" style="right:170px;top:64px;text-align:right;">
    <div class="ar">412 شارع الأرز</div><div class="ar">بروكفيلد 52810</div>
    <div style="margin-top:3px">412 Cedar Row</div><div>Brookfield, Ontario 52810</div>
  </div>
  <div class="divider" style="left:165px;top:62px;height:47px"></div>
  <div class="person" style="position:absolute;left:179px;top:66px;">
    <div class="name">SAMER HADDAD</div>
    <div class="role">President</div>
    <div class="name-ar">سامر حداد</div>
    <div class="role-ar">رئيس</div>
  </div>
  <div class="row-contacts" style="top:116px;">
    <span><svg><use href="#i-phone"/></svg>555-014-2671</span>
    <span><svg><use href="#i-mobile"/></svg>555-018-3392</span>
    <span><svg><use href="#i-fax"/></svg>555-016-4470</span>
    <span><svg><use href="#i-mail"/></svg>hello@nexoracognitive.com</span>
  </div>
  <div class="band" style="top:136px;height:12px;"><div class="web" style="padding-left:64px">WWW.NEXORACOGNITIVE.COM</div><div class="tail"></div></div>
</section>
<div class="label" style="left:932px;top:662px;">EMAIL SIGNATURE 2</div>

<!-- SOCIAL COVER 1 -->
<section class="piece cover" style="left:89px;top:691px;width:483px;height:184px;">
  <div class="tab"><div class="logo" style="left:14px;top:21px;font-size:8.5px;"><span class="dot" style="width:15px;height:15px"></span>Nexora Cognitive Systems</div></div>
  <h2>ARTIFICIAL<br>INTELLIGENCE</h2>
  <p>From toothbrush to TV and cars to space technology AI is everywhere and our expertise in AI will take you toward success.</p>
  <div class="art" role="img" aria-label="Large brand symbol decoration in white" style="left:230px;top:0;width:253px;height:184px;background:linear-gradient(120deg,rgba(255,255,255,0) 0%,rgba(255,255,255,.18) 55%,rgba(255,255,255,.08) 100%);"></div>
</section>
<div class="label" style="left:332px;top:886px;">SOCIAL COVER 1</div>

<!-- SOCIAL COVER 2 -->
<section class="piece cover" style="left:606px;top:691px;width:483px;height:184px;background:linear-gradient(90deg,#1579c3 0%,#0f86cf 60%,#1a9ad9 100%);">
  <div class="tab"><div class="logo" style="left:14px;top:21px;font-size:8.5px;"><span class="dot" style="width:15px;height:15px"></span>Nexora Cognitive Systems</div></div>
  <h2>ARTIFICIAL<br>INTELLIGENCE</h2>
  <p>From toothbrush to TV and cars to space technology AI is everywhere and our expertise in AI will take you toward success.</p>
  <div class="art" role="img" aria-label="Glowing network-mesh illustration of a running animal" style="left:170px;top:0;width:313px;height:184px;background:radial-gradient(ellipse at 65% 45%,rgba(120,225,255,.55) 0%,rgba(60,180,240,.25) 45%,rgba(20,130,210,0) 75%);"></div>
</section>
<div class="label" style="left:853px;top:886px;">SOCIAL COVER 2</div>

<!-- NETWORK PROFILE -->
<section class="piece profile" style="left:214px;top:915px;width:781px;height:219px;">
  <div class="banner"></div>
  <div class="art" role="img" aria-label="Large brand symbol decoration in deep blue tones" style="left:0;top:0;width:230px;height:132px;background:linear-gradient(120deg,#0e57a8 0%,#1a2fb0 45%,rgba(18,117,189,0) 100%);"></div>
  <h2>ARTIFICIAL INTELLIGENCE</h2>
  <div class="sub">From toothbrush to TV and cars to space technology<br>AI is everywhere and our expertise in AI will take you toward success.</div>
  <div class="avatar"><span class="dot" style="width:30px;height:30px;border-radius:50%;background:var(--blue);display:block"></span></div>
  <div class="logo" style="left:106px;top:140px;font-size:12px;">Nexora Cognitive Systems</div>
  <div class="btn follow">+ Follow</div>
  <div class="btn visit">Visit website&nbsp;
    <svg width="9" height="9" viewBox="0 0 10 10" fill="none" stroke="currentColor" stroke-width="1.4"><path d="M4 1H1v8h8V6M6 1h3v3M9 1 4.5 5.5"/></svg>
  </div>
  <div class="see-all">See all 9,999 employees on LinkUp &rarr;</div>
</section>
<div class="label" style="left:609px;top:1149px;">NETWORK PROFILE</div>

</body>
</html>
```